TLPB Business Card Design

Business card for sole operator professional civil and traffic engineer.
Clients are developers and planners who require assistance with traffic strategic master planning advice and design development for access and infrastructure associated with the development.
Colours already in use are greens for the business name and black for other legend. The attached file shows the letterhead template which is currently in use.
Target Market(s)
Professional Clients in development industry
Most clients known to the Principal and card is mostly required to allow ongoing contact
Industry/Entity Type
Business
Contact Information for Business Card
DESMOND HALVERTON CONSULTING SERVICES
ABN 37 818 502 194
PO Box 871 KERRAWAY NSW 2619
Desmond Halverton 0431 558 906
desmond.halverton@quillmarsh.net

```html
<!DOCTYPE html>
<html lang="en">
<head>
<meta charset="utf-8">
<title>TLPB Business Card</title>
<link rel="stylesheet" href="https://fonts.googleapis.com/css2?family=Ubuntu:wght@300;400;700&display=swap">
<style>
  :root {
    --page: #e9e7e2;
    --card: #0d0d0d;
    --card-glow: #2a2a2a;
    --green: #9fd25a;
    --grey: #9a9a9a;
  }
  html, body {
    margin: 0;
    width: 1200px;
    height: 1023px;
    overflow: hidden;
    background: var(--page);
    font-family: "Ubuntu", sans-serif;
  }
  .card {
    position: absolute;
    left: 150px;
    top: 226px;
    width: 900px;
    height: 570px;
    border-radius: 34px;
    background: radial-gradient(ellipse at 45% 55%, var(--card-glow) 0%, var(--card) 70%);
    overflow: hidden;
  }
  .brand {
    position: absolute;
    top: 62px;
    left: 0;
    width: 100%;
    text-align: center;
  }
  .brand-mark {
    display: inline-flex;
    align-items: center;
    gap: 14px;
    color: var(--green);
    font-weight: 700;
    font-size: 76px;
    letter-spacing: 2px;
    line-height: 1;
  }
  .brand-dot {
    width: 22px;
    height: 22px;
    border-radius: 50%;
    background: var(--green);
  }
  .company-name {
    margin-top: 14px;
    color: var(--green);
    font-weight: 700;
    font-size: 34px;
    letter-spacing: 0.5px;
  }
  .company-tag {
    margin-top: 4px;
    color: var(--grey);
    font-weight: 300;
    font-size: 24px;
    letter-spacing: 1.5px;
  }
  .name-rule {
    position: absolute;
    top: 284px;
    left: 0;
    width: 100%;
    display: flex;
    align-items: center;
    gap: 18px;
  }
  .name-rule::before,
  .name-rule::after {
    content: "";
    flex: 1;
    height: 1.5px;
    background: var(--green);
  }
  .person-name {
    color: var(--green);
    font-weight: 700;
    font-size: 28px;
    letter-spacing: 0.5px;
  }
  .contact {
    position: absolute;
    top: 338px;
    left: 0;
    width: 100%;
    text-align: center;
    color: var(--grey);
    font-weight: 400;
    font-size: 24px;
    line-height: 1.7;
  }
  .sweep {
    position: absolute;
    left: 0;
    top: 0;
  }
  .address {
    fill: var(--green);
    font-family: "Ubuntu", sans-serif;
    font-weight: 700;
    font-size: 26px;
    letter-spacing: 0.5px;
  }
</style>
</head>
<body>
  <div class="card">
    <div class="brand">
      <div class="brand-mark"><span class="brand-dot"></span>TLPB</div>
      <div class="company-name">DESMOND HALVERTON</div>
      <div class="company-tag">CONSULTING SERVICES</div>
    </div>

    <div class="name-rule"><span class="person-name">DESMOND HALVERTON</span></div>

    <div class="contact">
      <div class="phone">0431 558 906</div>
      <div class="email">desmond.halverton@quillmarsh.net</div>
    </div>

    <svg class="sweep" width="900" height="570" viewBox="0 0 900 570" aria-hidden="false">
      <path d="M 30 548 Q 450 440 880 556" fill="none" stroke="var(--green)" stroke-width="3"/>
      <path id="address-curve" d="M 80 522 Q 450 424 830 530" fill="none"/>
      <text class="address"><textPath href="#address-curve" startOffset="50%" text-anchor="middle">PO BOX 871 KERRAWAY NSW 2619</textPath></text>
    </svg>
  </div>
</body>
</html>
```